Consulting company (stride-and-calm, previously stundenwerk lübeck) needs design for a clear and fre

This website is to be made completely new with Worpreess / Divi. I am at the beginning and have no idea about the design. The design is the focus of this order. After the first website I would like to use the design and colors for all other design products for business, which will be placed here as well.
On the website the services, the team, references ... should be separate pages. Please see the attached document. A very important part is the blog and the categories should be visible in the desktop view, vie widgets.

The site should be clear, well-arranged, but still convey freshness and vitality.
Our company offers consulting and online trainings for the following topics:
- Digital paperless office
- process optimization, digitalization
- Remote working and productivity
- Remote leadership
- remote project management
- Time management 4. 0
- Focus on the essentials

We do this in the form of:
- Keynote Speaking
- Facilitating
- Presentation
- Workshops and trainings
- Online trainings

Our services are intended exclusively for companies.

What drives us?
We want to inspire our customers to work more green, lean digital and focus on the essentials. We are a team of three people who are digital nomads, but who also work offline on site.
I do have already webseites, but they are old, but give you an idea what we do: stundenwerk-luebeck.example. and ms-inkfree.example.

One style of a web site I like is for example is that of "plenvoro.example" Colors I thought so far, but I'm not sure, could be the color palette "vandal pigment" from drafbel.example or something similar to # f60b80a and # 39dfa7. But I am open for other suggestions.
I love simple and clear fonts. I like this contemporary style of sites, where you get most of the content on the mobile devices by scrolling.

Target Market(s)

midsize and large businesses, decision maker

Logo Text

Let's work green lean digital

Number of Pages Required

5+ page

Font styles to use
Sans Serif

Colors
e34297
00a990

Requirements
Must have
• the page should be clear and concise, much white with color accents like content blocks or headlines, responsive,
Nice to have
• I like interesting backgrounds, very discreet, perhaps white and gray or the color shades of pastel, the site should somehow fit to the photos, the logo I added is the old one, just to give you an idea
Should not have
• in no case too playful or loud

```html
<!DOCTYPE html>
<html lang="en">
<head>
<meta charset="utf-8">
<title>Ms. Inkfree – Consulting</title>
<link rel="stylesheet" href="https://fonts.googleapis.com/css2?family=Figtree:wght@400;500;600;700;800&display=swap">
<style>
:root{
  --pink:#e4429a;
  --pink-deep:#c9307f;
  --teal:#00a98f;
  --teal-dark:#00937c;
  --sky:#1eb4e6;
  --ink:#141414;
  --grey:#555;
  --light:#f2f2f2;
  --white:#fff;
}
*{box-sizing:border-box;margin:0;padding:0}
html,body{width:1200px;height:3980px;overflow:hidden}
body{position:relative;font-family:"Figtree",sans-serif;color:var(--ink);background:var(--white)}
.abs{position:absolute}
/* top bar */
.topbar{left:0;top:0;width:1200px;height:50px;background:var(--pink)}
.social{display:flex;gap:10px;position:absolute;left:50px;top:16px}
.social span{width:19px;height:19px;background:var(--white);opacity:.9;border-radius:2px}
.contact-line{position:absolute;right:52px;top:16px;color:var(--white);font-size:13px;display:flex;gap:28px;align-items:center}
.contact-line svg{vertical-align:middle;margin-right:8px}
/* header */
.brand{left:50px;top:80px;display:flex;align-items:center;gap:16px}
.brand .mark{width:72px;height:72px;background:var(--teal);border-radius:4px}
.brand .name{color:var(--teal);font-weight:700;font-size:30px;line-height:1}
.brand .name small{display:block;font-size:18px;font-weight:500;margin-bottom:4px}
.nav{right:52px;top:110px;display:flex;gap:18px;font-size:14px;font-weight:700;text-transform:uppercase}
.nav .active{border-bottom:2px solid var(--ink);padding-bottom:4px}
/* hero */
.hero{left:0;top:184px;width:1200px;height:536px;background:linear-gradient(100deg,#3a3a44 0%,#6d6c74 40%,#b8b4b0 70%,#dcd8d2 100%)}
.hero h1{position:absolute;left:50px;top:20px;color:var(--white);font-size:46px;font-weight:700;line-height:1.3;white-space:nowrap}
.hero .rule{position:absolute;left:50px;top:162px;width:36px;height:2px;background:var(--white)}
.hero p{position:absolute;left:50px;top:194px;color:var(--white);font-size:22px;font-weight:400;line-height:1.3;white-space:nowrap}
.btn-light{position:absolute;left:50px;top:320px;width:250px;height:50px;border-radius:25px;background:var(--white);color:var(--ink);font-weight:700;font-size:16px;display:flex;align-items:center;justify-content:center}
/* services */
.services{left:0;top:720px;width:1200px;height:500px;background:linear-gradient(90deg,rgba(214,54,140,.95),rgba(228,66,154,.92) 50%,rgba(214,54,140,.95));}
.section-title{font-size:34px;font-weight:700;text-align:center;text-transform:uppercase;width:1200px;left:0}
.services .section-title{color:var(--white);top:62px}
.service{position:absolute;top:150px;width:276px;text-align:center;color:var(--white)}
.service svg{display:block;margin:0 auto 48px}
.service h3{font-size:19px;font-weight:600;margin-bottom:16px}
.service p{font-size:13px;line-height:1.3;padding:0 18px}
.divider{position:absolute;top:210px;width:1px;height:200px;background:rgba(255,255,255,.7)}
/* benefits */
.benefit{position:absolute;top:1370px;width:230px}
.benefit .num{display:flex;align-items:center;gap:18px;color:var(--pink);font-weight:800;font-size:22px}
.benefit .num i{flex:1;height:1px;background:var(--pink)}
.benefit h3{margin-top:30px;font-size:23px;font-weight:700;line-height:1.3}
.benefit p{margin-top:28px;font-size:13px;line-height:1.33;color:#333}
.benefit a{display:block;margin-top:46px;color:var(--pink);font-weight:700;font-size:15px;text-decoration:none}
/* quote */
.quote{left:0;top:1757px;width:1200px;height:299px;background:var(--teal)}
.quote .portrait{position:absolute;left:187px;top:58px;width:180px;height:180px;border-radius:50%;background:radial-gradient(circle at 50% 40%,#e9e4dd,#9aa89c 70%,#3f7a4e);border:3px solid var(--white)}
.quote blockquote{position:absolute;left:446px;top:74px;width:570px;color:var(--white);font-size:17px;line-height:1.3}
.quote .sig-line{position:absolute;left:446px;top:206px;width:300px;height:1px;background:rgba(255,255,255,.8)}
.quote .sig{position:absolute;left:785px;top:185px;color:var(--white);font-size:33px;font-weight:700}
/* team */
.member{position:absolute;top:2253px;width:251px}
.member .photo{width:251px;height:398px;border:1px solid var(--teal);position:relative}
.member .icons{position:absolute;right:0;bottom:0;width:126px;height:48px;background:var(--teal);display:flex;gap:14px;align-items:center;justify-content:center}
.member .icons span{width:19px;height:19px;border:1px solid var(--white);border-radius:2px}
.member h4{margin-top:36px;color:var(--teal);font-size:22px;font-weight:700;text-transform:uppercase}
.member p{margin-top:6px;font-size:17px}
/* updates */
.updates{left:0;top:2828px;width:1200px;height:599px;background:linear-gradient(90deg,#d33b8c,#e4429a 50%,#d33b8c)}
.updates .section-title{color:var(--white);top:58px}
.card{position:absolute;top:143px;width:300px;height:400px;background:var(--white);padding:16px 18px}
.card .head{height:50px;color:var(--white);font-size:21px;font-weight:700;display:flex;align-items:center;justify-content:center}
.tweet{display:flex;gap:12px;padding:18px 8px 0;font-size:12.5px;line-height:1.35;border-bottom:1px solid #ccc;height:140px}
.tweet .dot{flex:none;width:30px;height:30px;border-radius:50%;background:var(--sky);margin-top:10px}
.tweet a{color:#1570c8;text-decoration:none}
.tweet small{display:block;color:#aaa;margin-top:20px;font-size:12px}
.article{display:flex;gap:12px;padding:12px 4px 0;border-bottom:1px solid #ccc;height:68px;font-size:12.5px;line-height:1.3}
.article .thumb{flex:none;width:30px;height:30px;border-radius:50%;background:linear-gradient(#d8d2c6,#5e7a5f)}
.article small{display:block;color:#aaa;font-size:11px}
.chev{display:block;margin:18px auto 0}
/* footer */
.footer{left:0;top:3427px;width:1200px;height:502px;background:var(--teal);color:var(--white)}
.footer .brand{left:77px;top:64px}
.footer .brand .mark{background:var(--white);width:72px;height:72px}
.footer .brand .name{color:var(--white)}
.footer .about{position:absolute;left:79px;top:162px;width:360px;font-size:12px;line-height:1.35}
.fcol{position:absolute;top:66px}
.fcol h5{font-size:22px;font-weight:700;margin-bottom:24px}
.fcol li{list-style:none;font-size:17px;margin-bottom:11px}
.footer .nl{position:absolute;left:79px;top:270px;font-size:16px;font-weight:700}
.footer .input{position:absolute;left:79px;top:307px;width:300px;height:48px;border:2px solid var(--white);font-size:13px;padding:14px 18px}
.footer .btn{position:absolute;left:79px;top:375px;width:300px;height:48px;background:var(--white);color:var(--ink);font-size:13px;font-weight:500;display:flex;align-items:center;justify-content:center}
.copyright{left:0;top:3929px;width:1200px;height:51px;background:#111;color:var(--white);font-size:16px;display:flex;align-items:center;justify-content:center}
</style>
</head>
<body>

<div class="abs topbar">
  <div class="social"><span></span><span></span><span></span><span></span><span></span><span></span></div>
  <div class="contact-line">
    <span><svg width="18" height="13" viewBox="0 0 18 13"><rect width="18" height="13" rx="1" fill="#fff"/><path d="M1 1l8 6 8-6" stroke="#e4429a" stroke-width="1.5" fill="none"/></svg>info@stundenwerk-luebeck.example</span>
    <span><svg width="17" height="17" viewBox="0 0 24 24"><path fill="#fff" d="M6.6 10.8a15 15 0 006.6 6.6l2.2-2.2c.3-.3.7-.4 1-.2 1.1.4 2.3.6 3.6.6.6 0 1 .4 1 1V20c0 .6-.4 1-1 1A17 17 0 013 4c0-.6.4-1 1-1h3.5c.6 0 1 .4 1 1 0 1.3.2 2.5.6 3.6.1.3 0 .7-.2 1z"/></svg>+49 000 1234 56 78</span>
  </div>
</div>

<div class="abs brand">
  <div class="mark"></div>
  <div class="name"><small>Ms.</small>INKFREE</div>
</div>
<nav class="abs nav">
  <span class="active">Services</span><span>Blog</span><span>Tips &amp; Trick</span><span>Testimonial</span><span>About us</span><span>Contact</span>
</nav>

<section class="abs hero" role="img" aria-label="Photo of a consultant working on a laptop in a bright office">
  <h1>For every minutes spent in organizing,<br>an hour is earned.</h1>
  <div class="rule"></div>
  <p>We want to inspire our customers to work more green,<br>lean digital and focus on the essentials.</p>
  <div class="btn-light">MORE DETAILS</div>
</section>

<section class="abs services" role="img" aria-label="Pink toned photo of a consultant behind the services overview">
  <h2 class="abs section-title">Our Services</h2>
  <div class="service" style="left:48px">
    <svg width="100" height="92" viewBox="0 0 100 92" fill="none" stroke="#fff" stroke-width="3"><path d="M4 2v84h94" /><path d="M4 86h94" stroke-dasharray="12 6"/><polyline points="22,60 42,40 62,52 86,28"/><circle cx="22" cy="60" r="5"/><circle cx="42" cy="40" r="5"/><circle cx="62" cy="52" r="5"/><circle cx="86" cy="28" r="5"/></svg>
    <h3>Paperless Office</h3><p>Change the appearance of your widgets in just several clicks of your mouse and enjoy the uniqueness of your business website.</p>
  </div>
  <div class="divider" style="left:325px"></div>
  <div class="service" style="left:324px">
    <svg width="100" height="92" viewBox="0 0 100 92" fill="none" stroke="#fff" stroke-width="3"><circle cx="50" cy="10" r="8"/><path d="M36 34c0-8 6-14 14-14s14 6 14 14"/><path d="M20 40h60"/><path d="M30 40v14M70 40v14"/><circle cx="28" cy="76" r="12"/><circle cx="72" cy="76" r="12"/><path d="M44 60h12"/></svg>
    <h3>Paperless Office</h3><p>Change the appearance of your widgets in just several clicks of your mouse and enjoy the uniqueness of your business website.</p>
  </div>
  <div class="divider" style="left:610px"></div>
  <div class="service" style="left:600px">
    <svg width="100" height="92" viewBox="0 0 100 92" fill="none" stroke="#fff" stroke-width="3"><rect x="6" y="4" width="88" height="56"/><rect x="14" y="10" width="72" height="44"/><rect x="26" y="34" width="8" height="14"/><rect x="42" y="26" width="8" height="22"/><rect x="58" y="18" width="8" height="30"/><path d="M34 60l-10 30M66 60l10 30"/></svg>
    <h3>Paperless Office</h3><p>Change the appearance of your widgets in just several clicks of your mouse and enjoy the uniqueness of your business website.</p>
  </div>
  <div class="divider" style="left:877px"></div>
  <div class="service" style="left:876px">
    <svg width="100" height="92" viewBox="0 0 100 92" fill="none" stroke="#fff" stroke-width="3"><circle cx="14" cy="22" r="8"/><circle cx="86" cy="22" r="8"/><path d="M6 70V44c0-6 4-10 10-10M94 70V44c0-6-4-10-10-10"/><path d="M16 50l10 8-10 14M84 50l-10 8 10 14"/><rect x="34" y="2" width="32" height="24" rx="2"/><path d="M44 26l-4 8 10-8"/></svg>
    <h3>Paperless Office</h3><p>Change the appearance of your widgets in just several clicks of your mouse and enjoy the uniqueness of your business website.</p>
  </div>
</section>

<section class="benefits">
  <h2 class="abs section-title" style="top:1282px">Your Benefits</h2>
  <div class="benefit" style="left:71px"><div class="num">01<i></i></div><h3>GREEN LEAN<br>DIGITAL OFFICE</h3><p>Lean work processes provide the platform for efficient work. Constant and ongoing process improvement is needed to ensure success and remain competitive. We help you achieve this.</p><a>READ MORE</a></div>
  <div class="benefit" style="left:352px"><div class="num">02<i></i></div><h3>GREEN LEAN<br>DIGITAL OFFICE</h3><p>Lean work processes provide the platform for efficient work. Constant and ongoing process improvement is needed to ensure success and remain competitive. We help you achieve this.</p><a>READ MORE</a></div>
  <div class="benefit" style="left:627px"><div class="num">03<i></i></div><h3>GREEN LEAN<br>DIGITAL OFFICE</h3><p>Lean work processes provide the platform for efficient work. Constant and ongoing process improvement is needed to ensure success and remain competitive. We help you achieve this.</p><a>READ MORE</a></div>
  <div class="benefit" style="left:904px"><div class="num">04<i></i></div><h3>GREEN LEAN<br>DIGITAL OFFICE</h3><p>Lean work processes provide the platform for efficient work. Constant and ongoing process improvement is needed to ensure success and remain competitive. We help you achieve this.</p><a>READ MORE</a></div>
</section>

<section class="abs quote">
  <div class="portrait" role="img" aria-label="Portrait of the company founder"></div>
  <blockquote>Thereby developing of ideas and concepts are in my same favor as gripped field work straightforwardly. I like to experience how colleagues and customers breathe a sigh of relief, pick up their courage and regain their fun working in the office.</blockquote>
  <div class="sig-line"></div>
  <div class="sig">Marta Velling</div>
</section>

<section class="team">
  <h2 class="abs section-title" style="top:2118px">Who Are We</h2>
  <div class="member" style="left:102px">
    <div class="photo" role="img" aria-label="Portrait of a team member in a suit" style="background:linear-gradient(#f4f4f4 55%,#2c3550)"><div class="icons"><span></span><span></span><span></span></div></div>
    <h4>Jonas Reller</h4><p>Head of Development</p>
  </div>
  <div class="member" style="left:474px">
    <div class="photo" role="img" aria-label="Portrait of a team member seated in an office chair" style="background:linear-gradient(#e6e4df 50%,#1e2433)"><div class="icons"><span></span><span></span><span></span></div></div>
    <h4>Jonas Reller</h4><p>Head of Development</p>
  </div>
  <div class="member" style="left:833px">
    <div class="photo" role="img" aria-label="Portrait of a team member in a black blazer" style="background:linear-gradient(#fafafa 50%,#1a1a1a)"><div class="icons"><span></span><span></span><span></span></div></div>
    <h4>Jonas Reller</h4><p>Head of Development</p>
  </div>
</section>

<section class="abs updates" role="img" aria-label="Pink toned photo of a consultant behind the latest updates">
  <h2 class="abs section-title">Our Latest Updates</h2>
  <div class="card" style="left:192px">
    <div class="head" style="background:var(--sky)">Latest Tweets</div>
    <div class="tweet"><span class="dot"></span><div>Get my organizing Services for free dream: I want to learn more about Europe and the rest of the world.<br><a>https://lnk.example/a1b2c3</a><small>about a day ago</small></div></div>
    <div class="tweet"><span class="dot"></span><div>Get my organizing Services for free dream: I want to learn more about Europe and the rest of the world.<br><a>https://lnk.example/a1b2c3</a><small>about a day ago</small></div></div>
    <svg class="chev" width="18" height="11" viewBox="0 0 18 11"><path d="M2 2l7 7 7-7" stroke="#333" stroke-width="3" fill="none"/></svg>
  </div>
  <div class="card" style="left:712px">
    <div class="head" style="background:var(--teal)">Recent Articles</div>
    <div class="article"><span class="thumb"></span><div>Creating Kaizen Culture<small>20 August 2014</small></div></div>
    <div class="article"><span class="thumb"></span><div>Pomodoro technique-extra boost to productivity<small>20 August 2014</small></div></div>
    <div class="article"><span class="thumb"></span><div>Creating Kaizen Culture<small>20 August 2014</small></div></div>
    <div class="article"><span class="thumb"></span><div>Pomodoro technique-extra boost to productivity<small>20 August 2014</small></div></div>
    <svg class="chev" width="18" height="11" viewBox="0 0 18 11"><path d="M2 2l7 7 7-7" stroke="#333" stroke-width="3" fill="none"/></svg>
  </div>
</section>

<footer class="abs footer">
  <div class="abs brand"><div class="mark"></div><div class="name"><small>Ms.</small>INKFREE</div></div>
  <p class="about">is a contemporary solution for both you and ourselves to engage in initial dialogue and coaching and follow-up discussions.</p>
  <div class="fcol" style="left:544px"><h5>NAVIGATE</h5><ul><li>Price Drop</li><li>New Products</li><li>Best Sales</li><li>Featured</li></ul></div>
  <div class="fcol" style="left:789px"><h5>SERVICES</h5><ul><li>Marketplace</li><li>Our Projects</li><li>New Reviews</li><li>Refunds</li></ul></div>
  <div class="fcol" style="left:1021px"><h5>CONTACT</h5><ul><li>Personal Info</li><li>Orders</li><li>Credit Cards</li><li>Addresses</li></ul></div>
  <div class="nl">SUBSCRIBE TO OUR NEWSLETTER</div>
  <div class="input">Enter your email address</div>
  <div class="btn">SUBSCRIBE NOW</div>
</footer>
<div class="abs copyright">Copyright 2020 | Ms. Inkfree. All rights reserved</div>

</body>
</html>
```